Mac IT Support company needs a flyer

This flyer will be delivered by hand to prospective customers in a door drop campaign.
Double sided A6
We support SMEs in Central London mainly Mac networks. We also supply managed services including email and internet connectivity.
The target audience is office managers, receptionists and business owners.
It will be extremely simple and illustration mainly.
Any ideas are welcome but we quite like the following:
A text poster saying
"Make IT easy" or something like that.
An illustration of two people, the client and us. Us juggling web, IT etc and the Client able to concentrate on their job.
Copy is being written by a professional copywriter, content of which will depend on the flyer design.
Target Market(s)
Small SMEs using Orchard Mac computers, design companies, agencies etc.
Industry/Entity Type
Technical Service
Requirements
Must have
- Our number - 0207 946 0581
- Our email - info@brightloop.example
- Our web address - www.brightloop.example
Nice to have
- Some clever eye catching designs
Should not have
- Too much text
- Overly complicated design

```html
<!DOCTYPE html>
<html lang="en">
<head>
<meta charset="utf-8">
<title>BrightLoop – Make IT Easy flyer</title>
<link rel="stylesheet" href="https://fonts.googleapis.com/css2?family=Lato:wght@400;700&family=Oswald:wght@600&family=Roboto:wght@400&display=swap">
<style>
  :root {
    --lime: #a8cf38;
    --charcoal: #231f20;
    --paper: #ffffff;
    --ink: #1e1b1c;
    --hex: #4a4647;
  }
  * { margin: 0; padding: 0; box-sizing: border-box; }
  html, body { width: 900px; height: 1200px; overflow: hidden; background: var(--paper); }
  .canvas { position: relative; width: 900px; height: 1200px; background: var(--paper); }
  .flyer {
    position: absolute; left: 122px; top: 139px; width: 654px; height: 920px;
    background: var(--charcoal); overflow: hidden;
    font-family: "Lato", sans-serif;
  }
  .flyer-shapes { position: absolute; left: 0; top: 0; width: 654px; height: 920px; }
  .brand-name {
    position: absolute; left: 20px; top: 46px;
    font-family: "Lato", sans-serif; font-weight: 700; font-size: 46px;
    color: var(--lime); letter-spacing: -0.5px;
  }
  .headline { position: absolute; left: 16px; top: 366px; color: var(--paper); }
  .headline-light {
    display: block; font-family: "Roboto", sans-serif; font-weight: 400;
    font-size: 74px; line-height: 76px; color: var(--paper); letter-spacing: -1px;
  }
  .headline-bold {
    display: block; font-family: "Oswald", sans-serif; font-weight: 600;
    font-size: 96px; line-height: 98px; color: var(--ink); letter-spacing: 5px;
  }
  .about {
    position: absolute; left: 21px; top: 688px; width: 260px;
    font-size: 14.6px; line-height: 19.4px; color: var(--ink);
    text-align: justify; hyphens: auto;
  }
  .services { position: absolute; left: 330px; top: 511px; list-style: none; }
  .service { position: relative; height: 49.5px; padding-left: 53px; }
  .service-icon { position: absolute; left: 0; top: 3px; width: 36px; height: 38px; }
  .service-title { display: block; color: var(--lime); font-weight: 700; font-size: 17px; line-height: 22px; }
  .service-text { display: block; color: var(--paper); font-size: 17px; line-height: 22px; }
  .contact-bar {
    position: absolute; left: 0; bottom: 0; width: 654px; height: 46px;
    background: var(--lime); display: flex; align-items: center;
    justify-content: space-between; padding: 0 18px 0 30px;
    color: var(--paper); font-size: 17px; white-space: nowrap;
  }
  .contact-item { display: flex; align-items: center; gap: 7px; flex: none; }
  .contact-icon { width: 18px; height: 18px; flex: none; }
  .contact-icon-mail { width: 22px; }
</style>
</head>
<body>
<div class="canvas">
  <section class="flyer">
    <svg class="flyer-shapes" viewBox="0 0 654 920">
      <defs>
        <linearGradient id="meetingTones" x1="0" y1="0" x2="1" y2="1">
          <stop offset="0" stop-color="#6f8a5a"/>
          <stop offset="0.5" stop-color="#b9b3a3"/>
          <stop offset="1" stop-color="#e4e2dc"/>
        </linearGradient>
      </defs>
      <polygon role="img" aria-label="Photo: business people shaking hands across a meeting table with a laptop"
               points="298,0 654,0 654,305 468,439 63,236" fill="url(#meetingTones)"/>
      <polygon class="accent-green" points="0,280 63,236 468,439 0,672" fill="var(--lime)"/>
      <polygon class="about-panel" points="0,690 268,574 318,874 0,874" fill="var(--paper)"/>
      <polygon class="accent-stripe" points="262,548 272,545 330,874 318,874" fill="var(--lime)"/>
    </svg>

    <div class="brand-name">BrightLoop</div>

    <h1 class="headline">
      <span class="headline-light">MAKE IT</span>
      <span class="headline-bold">EASY</span>
    </h1>

    <p class="about">BrightLoop was formed in 2004 as an IT support company servicing London's advertising and media companies. In the last 11 years we've grown to support all three major platforms: Orchard, Panes and Tuxen. We now support a far wider demographic including Finance, Retail, Governing bodies and Property to name just a few.</p>

    <ul class="services">
      <li class="service">
        <svg class="service-icon" viewBox="0 0 36 38"><polygon points="18,1 34,10 34,28 18,37 2,28 2,10" fill="var(--hex)"/><circle cx="18" cy="19" r="8" fill="none" stroke="var(--lime)" stroke-width="3"/></svg>
        <span class="service-title">Cloud Based Backup</span><span class="service-text">Backup your data to the cloud</span>
      </li>
      <li class="service">
        <svg class="service-icon" viewBox="0 0 36 38"><polygon points="18,1 34,10 34,28 18,37 2,28 2,10" fill="var(--hex)"/><ellipse cx="18" cy="19" rx="10" ry="6" fill="var(--lime)"/><circle cx="18" cy="19" r="3" fill="var(--hex)"/></svg>
        <span class="service-title">Cloud Based Email Hosting</span><span class="service-text">Move your email into the cloud</span>
      </li>
      <li class="service">
        <svg class="service-icon" viewBox="0 0 36 38"><polygon points="18,1 34,10 34,28 18,37 2,28 2,10" fill="var(--hex)"/><path d="M18 9 L26 12 L26 19 Q26 26 18 29 Q10 26 10 19 L10 12 Z" fill="var(--lime)"/></svg>
        <span class="service-title">Internet Connectivity</span><span class="service-text">Broadband and fibre internet</span>
      </li>
      <li class="service">
        <svg class="service-icon" viewBox="0 0 36 38"><polygon points="18,1 34,10 34,28 18,37 2,28 2,10" fill="var(--hex)"/><path d="M11 25 Q6 25 7 20 Q8 16 12 17 Q13 11 19 11 Q25 11 25 17 Q30 17 29 22 Q28 25 25 25 Z" fill="var(--lime)"/><path d="M18 24 V17 M15 20 L18 17 L21 20" stroke="var(--hex)" stroke-width="2" fill="none"/></svg>
        <span class="service-title">Spam Prevention</span><span class="service-text">99% email spam prevented</span>
      </li>
      <li class="service">
        <svg class="service-icon" viewBox="0 0 36 38"><polygon points="18,1 34,10 34,28 18,37 2,28 2,10" fill="var(--hex)"/><circle cx="18" cy="17" r="8" fill="none" stroke="var(--lime)" stroke-width="2"/><circle cx="18" cy="17" r="3" fill="var(--lime)"/><rect x="17" y="20" width="2" height="9" fill="var(--lime)"/></svg>
        <span class="service-title">Relocation</span><span class="service-text">Manage your IT move</span>
      </li>
      <li class="service">
        <svg class="service-icon" viewBox="0 0 36 38"><polygon points="18,1 34,10 34,28 18,37 2,28 2,10" fill="var(--hex)"/><rect x="9" y="13" width="18" height="12" fill="var(--lime)"/><path d="M9 13 L18 20 L27 13" stroke="var(--hex)" stroke-width="1.5" fill="none"/></svg>
        <span class="service-title">IT Support</span><span class="service-text">Remote and onsite</span>
      </li>
      <li class="service">
        <svg class="service-icon" viewBox="0 0 36 38"><polygon points="18,1 34,10 34,28 18,37 2,28 2,10" fill="var(--hex)"/><rect x="9" y="14" width="6" height="13" fill="var(--lime)"/><rect x="21" y="11" width="6" height="16" fill="var(--lime)"/><path d="M15 19 H21" stroke="var(--lime)" stroke-width="2"/></svg>
        <span class="service-title">Monitoring</span><span class="service-text">For all IT systems</span>
      </li>
    </ul>

    <footer class="contact-bar">
      <span class="contact-item">
        <svg class="contact-icon" viewBox="0 0 20 20"><rect x="3" y="2" width="14" height="16" rx="3" fill="var(--charcoal)"/><path d="M7 6 Q6 11 11 14 L13 12" stroke="var(--lime)" stroke-width="2" fill="none"/></svg>
        <span class="contact-text">0207 946 0581</span>
      </span>
      <span class="contact-item">
        <svg class="contact-icon" viewBox="0 0 20 20"><g fill="none" stroke="var(--charcoal)" stroke-width="1.6"><circle cx="10" cy="10" r="8"/><ellipse cx="10" cy="10" rx="3.5" ry="8"/><path d="M2 10 H18 M4 5.5 H16 M4 14.5 H16"/></g></svg>
        <span class="contact-text">www.brightloop.example</span>
      </span>
      <span class="contact-item">
        <svg class="contact-icon contact-icon-mail" viewBox="0 0 24 20"><rect x="1" y="4" width="22" height="13" fill="var(--charcoal)"/><path d="M1 4 L12 12 L23 4" stroke="var(--lime)" stroke-width="1.5" fill="none"/></svg>
        <span class="contact-text">info@brightloop.example</span>
      </span>
    </footer>
  </section>
</div>
</body>
</html>
```